Etiketten für kalt gepresste Bio-Öle
Zielgruppe
Wir sind ein Bio-Betrieb, der sowohl Gemüse anbaut, als auch gesunde Bio-Lebensmittel herstellt. Gründungsjahr: 1999 - Jetzt werden wir eine Ölmühle dazubekommen und auch frische, kalt gepresste Bio-Öle anbieten. Dazu brauchen wir ein hochwertiges Etikettendesign am Beispiel des Leinöls. Die Öle sind im höheren Preissegment (z.B. 500 ml Leinöl für 17,90 €)
Unsere Zielgruppe sind gesundheitsbewusste Menschen mittleren Einkommens. In der Regel kennen sich unsere Kunden in Ernährungsfragen aus und haben einen hohen Qualitätsanspruch.
Aufgabenstellung
Der Kreativität ist freier Raum gegeben. Was wir ausschließen sind anzügliche Begriffe oder Anspielungen. Es handelt sich um ein hochwertiges Produkt, das zwar den Öko-Aspekt beinhaltet, aber trotzdem modern rüberkommen sollte.
Folgende Inhalte muss das Etikett enthalten:
- Firmenlogo (Ölmanufaktur sun4seed - ein vorhandenes Logo ist hier nicht vorgegeben)
- Produktname (z.B. Leinöl - aus brauner Leinsaat)
- Bio-Siegel (DE-ÖKO-047 EU-/Nicht-EU-Landwirtschaft)
- Zutatenliste (z.B. 100% kalt gepresstes Bio-Leinöl aus brauner Leinsaat)
- Mindesthaltbarkeitsdatum
- Nährwertangeben (Brennwerte, Kohlenhydrate, Zucker, Fett, gesättigte Fettsäuren, Eiweiß, Salz)
- Barcode
- Füllmenge (z.B. 500 ml)
- Produktbeschreibung (siehe Dateiupload)
- Empfehlung (z.B. Das Leinöl ist ein Qualitätsprodukt. Es sollte frisch innerhalb von 3 Wochen verzehrt werden. Kühl und dunkel lagern.)
Die 500ml Flasche kann unter folgendem Link eingesehen werden:
https://www.vessoria.com/lumara-500ml-antikglas-mdg.-pp-482.html
Durchmesser 60,3 mm, Höhe 277,5 mm
Wichtig:
Bitte orientieren Sie sich NICHT an dem Design unserer Webseiten, da wir eine komplett neue Produktlinie aufbauen wollen.

```html
<!DOCTYPE html>
<html lang="de">
<head>
<meta charset="utf-8">
<title>sun4seed Ölmanufaktur – Leinöl Etikett</title>
<link href="https://fonts.googleapis.com/css2?family=Dancing+Script:wght@600&family=Roboto:wght@400;500&display=swap" rel="stylesheet">
<style>
  :root {
    --backdrop: #b2a5bb;
    --label-white: #ffffff;
    --label-purple: #9a7cc0;
    --label-purple-light: #ad94cf;
    --label-purple-dark: #8c6db4;
    --ink: #1c1a1e;
    --type-light: #ffffff;
    --type-soft: #efe6f8;
    --art-tone: #b59dd3;
  }
  html, body {
    margin: 0;
    padding: 0;
    width: 706px;
    height: 1200px;
    overflow: hidden;
    background: var(--backdrop);
  }
  .label {
    position: absolute;
    left: 73px;
    top: 80px;
    width: 560px;
    height: 1040px;
    background: linear-gradient(90deg, var(--label-purple-light) 0%, var(--label-purple) 45%, var(--label-purple-dark) 100%);
    overflow: hidden;
  }
  .label__header {
    position: absolute;
    left: 0;
    top: 0;
    width: 560px;
    height: 240px;
  }
  .label__wave {
    position: absolute;
    left: 0;
    top: 0;
  }
  .brand {
    position: absolute;
    left: 0;
    right: 0;
    top: 52px;
    text-align: center;
    color: var(--ink);
    font-family: "Roboto", sans-serif;
  }
  .brand__name {
    font-weight: 500;
    font-size: 58px;
    line-height: 1;
    letter-spacing: 1px;
  }
  .brand__tagline {
    margin-top: 12px;
    font-weight: 400;
    font-size: 24px;
    letter-spacing: 6px;
  }
  .flax-art {
    position: absolute;
    left: 68px;
    top: 390px;
    width: 395px;
    height: 250px;
    border-radius: 50%;
    background: radial-gradient(ellipse at center, var(--art-tone) 0%, rgba(181,157,211,0.35) 55%, rgba(181,157,211,0) 75%);
  }
  .product {
    position: absolute;
    left: 0;
    right: 0;
    top: 700px;
    text-align: center;
  }
  .product__name {
    margin: 0;
    font-family: "Dancing Script", cursive;
    font-weight: 600;
    font-size: 122px;
    line-height: 1.1;
    color: var(--type-light);
  }
  .product__origin {
    margin: 18px 0 0;
    font-family: "Roboto", sans-serif;
    font-weight: 400;
    font-size: 32px;
    letter-spacing: 0.5px;
    color: var(--type-soft);
  }
</style>
</head>
<body>
  <main class="label">
    <header class="label__header">
      <svg class="label__wave" width="560" height="240" viewBox="0 0 560 240" aria-hidden="true">
        <path d="M0 0 H560 V182 C470 176 400 192 300 206 C200 222 100 236 0 234 Z" fill="var(--label-white)"/>
      </svg>
      <div class="brand">
        <div class="brand__name">sun4seed</div>
        <div class="brand__tagline">ÖLMANUFAKTUR</div>
      </div>
    </header>

    <div class="flax-art" role="img" aria-label="Zarte Linienzeichnung zweier Leinblüten mit Knospen und Samen"></div>

    <section class="product">
      <h1 class="product__name">Leinöl</h1>
      <p class="product__origin">AUS BRAUNER LEINSAAT</p>
    </section>
  </main>
</body>
</html>
```